Background of Our Business: TQB Financial Services provides accounting and tax services to small businesses. Website: www.tqbfsx.com.au. Our slogan is: one stop finance department service for small businesses.
I would like a flyer design with 2 sides.
1st side)
Business Logo; TQB - Finance Department Service for Small Businesses (Please refer file 1 as attached)

Large text of: Too many things going on? Smaller text: Let us reduce your input into accounts, you can focus on more value adding areas.

Our Services: Bookkeeping, Payroll, Financial Statement, Tax Advisory, Tax Return, Business Performance Measurement, Business Decision Support, Assistance in Loan Applications, and much more.

Why Us: Our clients are handpicked, we are fully committed to your business, and our works are performed at corporate standard. We utilise technology to save your accounting cost, monitor your compliance risks, provide solid data for business decision making, and be your representative in dealing with banks and NRB. (Please also refer file 2 as attached)

Contact details: Address: 58 Dunmore Street, Carlisle, WA 6101
PO Box 2493, East Victoria Park, WA 6981
Tel: (08) 6287 3914; Mob: 0491 738 226

2nd side)
Our Pricing: Charge by transaction volumes; Fixed fee advised beforehand. hourly rate please refer file 4 as attached.

Our 'Gold' level service subscriber receives:
Frequent bookkeeping, payroll, and financial reporting services
Integrate tax advisory, compliance risk monitoring and control
Free regular preliminary business performance check
Free assistance in commercial loan and mortgage application
Free hand picked business insights for your industry
Free representative service for you in dealing with banks, NRB.

Coupon Section: Sign up now and receive 10% off for your next 12 months bill. Valid until 31/07/2016.

```html
<!DOCTYPE html>
<html lang="en">
<head>
<meta charset="utf-8">
<title>TQB Financial Services – Two-sided Flyer</title>
<link rel="stylesheet" href="https://fonts.googleapis.com/css2?family=Ubuntu:wght@400;500;700&family=Open+Sans:wght@300;400;600&display=swap">
<style>
:root{
  --navy:#173f7a;
  --cyan:#33c0e3;
  --grey:#7c7c7c;
  --grey-text:#6b6b6b;
  --backdrop:#e4e4e4;
  --white:#ffffff;
  --kraft:#d9c9a4;
  --kraft-dark:#c9b78f;
}
*{margin:0;padding:0;box-sizing:border-box}
html,body{width:1200px;height:919px;overflow:hidden;background:var(--backdrop)}
body{font-family:"Open Sans",sans-serif}
.stage{position:relative;width:1500px;height:1149px;transform:scale(.8);transform-origin:0 0;
  background:radial-gradient(ellipse at center,#f2f2f2 0%,#dedede 100%)}
.page{position:absolute;top:87px;width:677px;height:957px;background:var(--white);overflow:hidden}
.page--front{left:61px}
.page--back{left:765px}
.abs{position:absolute}

/* brand */
.brand{display:flex;align-items:center;gap:10px}
.brand__mark{width:44px;height:44px;background:var(--navy)}
.brand__name{font-family:"Ubuntu",sans-serif;font-weight:500;color:var(--navy);font-size:58px;letter-spacing:2px;line-height:1}
.brand__tag{font-size:10.5px;color:var(--navy);border-top:1px solid #8aa0c2;padding-top:3px;margin-top:6px;white-space:nowrap}

/* front header */
.hero{left:0;top:0;width:677px;height:292px;background:linear-gradient(90deg,#fff 0%,#fafafa 45%,#ececec 100%)}
.hero__photo{right:0;top:0;width:290px;height:292px;
  background:linear-gradient(200deg,#f4e4c0 0%,#e8d2a6 45%,#d8c29a 75%,#efefef 100%)}
.hero__title{left:30px;top:128px;font-family:"Ubuntu",sans-serif;font-weight:500;font-size:47px;line-height:47px;color:var(--navy)}
.hero__lead{left:32px;top:226px;font-size:18.5px;line-height:25px;color:#222}

.band{top:292px;height:168px;color:var(--white);padding:16px 30px}
.band--services{left:0;width:268px;background:var(--navy)}
.band--why{left:268px;width:409px;background:var(--grey);padding-left:18px}
.band h2{font-family:"Ubuntu",sans-serif;font-weight:500;font-size:19px;margin-bottom:16px}
.band p{font-size:12.6px;line-height:16px}

.features{left:30px;top:476px;width:620px;display:grid;grid-template-columns:repeat(3,1fr);column-gap:18px;row-gap:16px}
.feature{text-align:center}
.feature__icon{width:58px;height:58px;border-radius:50%;background:var(--cyan);margin:0 auto 14px;display:flex;align-items:center;justify-content:center}
.feature h3{font-family:"Ubuntu",sans-serif;font-weight:400;font-size:15px;color:#444;margin-bottom:14px}
.feature p{font-size:10.2px;line-height:13.6px;color:var(--grey-text)}

.footer-front{top:873px;height:84px}
.footer-front__addr{left:0;width:425px;background:var(--grey);color:#fff;font-size:12.5px;line-height:20px;padding:20px 32px}
.footer-front__tel{left:425px;width:252px;background:var(--navy);color:#fff;font-family:"Ubuntu",sans-serif;font-size:22px;line-height:32px;padding:8px 15px}
.footer-front__tel b{font-weight:500}

/* back */
.pricing-hero{left:0;top:0;width:677px;height:190px;
  background:linear-gradient(100deg,#5d5a59 0%,#746f6c 40%,#9c9592 70%,#c8c1bb 100%)}
.pricing-hero__title{left:28px;top:40px;font-family:"Ubuntu",sans-serif;font-weight:500;font-size:54px;color:#fff;line-height:1}
.pricing-hero__sub{left:32px;top:104px;font-size:18.5px;color:#fff}
.tiers{left:0;top:190px;width:677px;height:220px;background:var(--cyan)}
.tier{position:absolute;color:#fff;padding:0 20px 0 24px}
.tier h2{font-family:"Ubuntu",sans-serif;font-weight:500;font-size:20px;text-align:center;line-height:28px}
.tier--bronze{left:0;top:20px;width:220px}
.tier--gold{left:220px;top:-32px;width:224px;height:252px;background:var(--navy);padding-top:12px}
.tier--plat{left:444px;top:20px;width:233px}
.tier__rule{border:0;border-top:2px solid #fff;margin:6px 0 8px}
.rates{font-size:11.3px;line-height:16px;width:100%}
.tier--gold .rates{font-size:12.3px}
.rates div{display:flex;justify-content:space-between}
.tier__note{font-size:10.8px;line-height:13.5px;margin-top:16px}

.benefits{left:36px;top:432px;width:610px}
.benefits h2{font-family:"Ubuntu",sans-serif;font-weight:400;font-size:28px;color:var(--navy);margin-bottom:14px}
.benefits li{list-style:none;font-size:18.3px;line-height:27.3px;color:#6a6a6a;font-weight:300;letter-spacing:-.1px}

.coupon{left:0;top:668px;width:677px;height:177px;background:linear-gradient(90deg,var(--kraft) 0%,#e1d3b1 50%,var(--kraft-dark) 100%)}
.coupon__frame{position:absolute;left:19px;top:16px;right:19px;bottom:14px;border:2px dashed #333;padding:12px 18px}
.coupon__offer{font-family:"Ubuntu",sans-serif;font-weight:500;font-size:35px;line-height:41px;color:var(--navy)}
.coupon__date{font-family:"Ubuntu",sans-serif;font-weight:500;font-size:21px;color:#333;margin-top:6px}

.footer-back{top:845px;height:112px}
.footer-back__brand{left:0;width:243px;background:#fff;padding:24px 0 0 38px}
.footer-back__brand .brand__mark{width:32px;height:32px}
.footer-back__brand .brand__name{font-size:40px}
.footer-back__brand .brand__tag{font-size:7.5px}
.footer-back__contact{left:243px;width:434px;background:var(--navy);color:#fff;font-size:12.8px;line-height:17px;padding:26px 46px}
.footer-back__contact b{font-weight:600}
</style>
</head>
<body>
<div class="stage">

  <!-- Front side -->
  <section class="page page--front">
    <div class="abs hero"></div>
    <div class="abs hero__photo" role="img" aria-label="Photo of a tall stack of paper files and documents"></div>
    <div class="abs" style="left:32px;top:30px">
      <div class="brand"><span class="brand__mark"></span><span class="brand__name">TQB</span></div>
      <div class="brand__tag">Finance Department Service for Small Businesses</div>
    </div>
    <h1 class="abs hero__title">TOO MANY THINGS<br>GOING ON?</h1>
    <p class="abs hero__lead">Let us reduce your input into accounts,<br>you can focus on more value adding areas.</p>

    <div class="abs band band--services">
      <h2>OUR SERVICES:</h2>
      <p>Bookkeeping, Payroll, Financial Statement, Tax Advisory, Tax Return, Business Performance Measurement, Business Decision Support, Assistance in Loan Applications, and much more.</p>
    </div>
    <div class="abs band band--why">
      <h2>WHY US:</h2>
      <p>Our clients are handpicked, we are fully committed to your business, and our works are performed at corporate standard. We utilise technology to save your accounting cost, monitor your compliance risks, provide solid data for business decision making, and be your representative in dealing with banks and NRB.</p>
    </div>

    <div class="abs features">
      <div class="feature">
        <div class="feature__icon"><svg width="28" height="28" viewBox="0 0 28 28"><rect x="3" y="3" width="22" height="22" rx="2" fill="#fff"/><circle cx="9" cy="10" r="2.5" fill="#33c0e3"/><rect x="13" y="8" width="9" height="2" fill="#33c0e3"/><rect x="6" y="15" width="16" height="2" fill="#33c0e3"/><rect x="6" y="19" width="16" height="2" fill="#33c0e3"/></svg></div>
        <h3>We work for you</h3>
        <p>We work like employees for your business, take responsibilities like employee does. You enjoy hassle free for your PAYG withholding, Superannuation Guarantee obligations, and leave entitlements.</p>
      </div>
      <div class="feature">
        <div class="feature__icon"><svg width="28" height="28" viewBox="0 0 28 28"><rect x="4" y="5" width="19" height="19" rx="3" fill="none" stroke="#fff" stroke-width="2.5"/><path d="M9 14l4 4 11-12" fill="none" stroke="#fff" stroke-width="3"/></svg></div>
        <h3>at Corporate Standard</h3>
        <p>We hire qualified professionals and invest heavily on training, along with our testified 'Preparation + Checklist + Review' structure, we meet industry aspiration at the best of our knowledge.</p>
      </div>
      <div class="feature">
        <div class="feature__icon"><svg width="30" height="30" viewBox="0 0 30 30"><circle cx="11" cy="16" r="6" fill="none" stroke="#fff" stroke-width="4" stroke-dasharray="3 2"/><circle cx="11" cy="16" r="2" fill="#fff"/><circle cx="21" cy="9" r="4" fill="none" stroke="#fff" stroke-width="3" stroke-dasharray="2 1.5"/><circle cx="21" cy="22" r="3.5" fill="none" stroke="#fff" stroke-width="3" stroke-dasharray="2 1.5"/></svg></div>
        <h3>Utilise Technology</h3>
        <p>We work with our clients as a team, we use technology to improve information sharing so that clients and us on the same page, and improve efficiency and productivity by following and utilizing technology advance.</p>
      </div>
      <div class="feature">
        <div class="feature__icon"><svg width="28" height="28" viewBox="0 0 28 28"><rect x="5" y="13" width="4" height="9" fill="#fff"/><rect x="11" y="7" width="4" height="15" fill="#fff"/><rect x="17" y="10" width="4" height="12" fill="#fff"/><rect x="4" y="22" width="20" height="2" fill="#fff"/></svg></div>
        <h3>Provide solid data</h3>
        <p>In the meantime of keeping your accounts, we will be maintaining your database from sales, purchases suppliers, customers, employees, and other stakeholders, which are helpful for decision making.</p>
      </div>
      <div class="feature">
        <div class="feature__icon"><svg width="28" height="28" viewBox="0 0 28 28"><rect x="4" y="6" width="20" height="18" rx="2" fill="none" stroke="#fff" stroke-width="2.5"/><rect x="4" y="6" width="20" height="5" fill="#fff"/><rect x="8" y="3" width="2" height="5" fill="#fff"/><rect x="18" y="3" width="2" height="5" fill="#fff"/><text x="14" y="21" text-anchor="middle" font-family="Ubuntu,sans-serif" font-size="9" font-weight="700" fill="#fff">15</text></svg></div>
        <h3>Monitor Compliance Risk</h3>
        <p>As we work as employee for your business, we take the responsibility to monitor and remind you for tax compliance requirement, and work together with you to fulfil the requirement.</p>
      </div>
      <div class="feature">
        <div class="feature__icon"><svg width="32" height="28" viewBox="0 0 32 28"><circle cx="16" cy="8" r="3.5" fill="#fff"/><rect x="12" y="12" width="8" height="11" rx="2" fill="#fff"/><circle cx="8" cy="10" r="2.8" fill="#fff"/><rect x="5" y="13.5" width="6" height="8" rx="2" fill="#fff"/><circle cx="24" cy="10" r="2.8" fill="#fff"/><rect x="21" y="13.5" width="6" height="8" rx="2" fill="#fff"/></svg></div>
        <h3>Your Finance Representative</h3>
        <p>With your consent, we will be dealing with NRB, financial institutions and other finance related stakeholders on your behalf for better efficiency and effectiveness, as we speak their business language.</p>
      </div>
    </div>

    <div class="abs footer-front footer-front__addr">Contact details: Address: 58 Dunmore Street, Carlisle, WA 6101<br>PO Box 2493, East Victoria Park, WA 6981</div>
    <div class="abs footer-front footer-front__tel">Tel: <b>(08) 6287 3914;</b><br>Mob: <b>0491 738 226</b></div>
  </section>

  <!-- Back side -->
  <section class="page page--back">
    <div class="abs pricing-hero" role="img" aria-label="Photo of hands working on a laptop keyboard"></div>
    <h1 class="abs pricing-hero__title">OUR PRICING</h1>
    <p class="abs pricing-hero__sub">Charge by transaction volumes; Fixed fee advised beforehand</p>

    <div class="abs tiers">
      <div class="tier tier--bronze">
        <h2>BRONZE</h2><hr class="tier__rule">
        <div class="rates">
          <div><span>Bookkeeping &amp; Payroll:</span><span>$50/hr</span></div>
          <div><span>Taxation:</span><span>$110/hr</span></div>
          <div><span>Management Accounting:</span><span>$110/hr</span></div>
          <div><span>Finance:</span><span>POA, Generally Free</span></div>
          <div><span>General Consulting:</span><span>Free*</span></div>
        </div>
        <p class="tier__note">Rate above applies for using us for bookkeeping or payroll or taxation or management accounting service only.</p>
      </div>
      <div class="tier tier--gold">
        <h2>GOLD<br>(MOST POPULAR)</h2><hr class="tier__rule">
        <div class="rates">
          <div><span>Bookkeeping &amp; Payroll:</span><span>$45/hr</span></div>
          <div><span>Taxation:</span><span>$99/hr</span></div>
          <div><span>Management Accounting:</span><span>$99/hr</span></div>
          <div><span>Finance:</span><span>POA. Generally Free</span></div>
          <div><span>General Consulting:</span><span>Free*</span></div>
        </div>
        <p class="tier__note">Rate above applies for using us for bookkeeping or payroll or management accounting and taxation services.</p>
      </div>
      <div class="tier tier--plat">
        <h2>PLANTIUM</h2><hr class="tier__rule">
        <div class="rates">
          <div><span>Bookkeeping &amp; Payroll:</span><span>$40/hr</span></div>
          <div><span>Taxation:</span><span>$88/hr</span></div>
          <div><span>Management Accounting:</span><span>$88/hr</span></div>
          <div><span>Finance:</span><span>POA, Generally Free</span></div>
          <div><span>General Consulting:</span><span>Free*</span></div>
        </div>
        <p class="tier__note">Rate above applies for using us for bookkeeping or payroll and taxation and management accounting services.</p>
      </div>
    </div>

    <div class="abs benefits">
      <h2>Our 'Gold' level service subscriber receives:</h2>
      <ul>
        <li>Frequent bookkeeping, payroll, and financial reporting services</li>
        <li>Integrate tax advisory, compliance risk monitoring and control</li>
        <li>Free regular preliminary business performance check</li>
        <li>Free assistance in commercial loan and mortgage application</li>
        <li>Free hand picked business insights for your industry</li>
        <li>Free representative service for you in dealing with banks, NRB.</li>
      </ul>
    </div>

    <div class="abs coupon">
      <div class="coupon__frame">
        <p class="coupon__offer">Sign up now and receive 10%<br>off for your next 12 months bill.</p>
        <p class="coupon__date">Valid until 31/07/2016.</p>
      </div>
    </div>

    <div class="abs footer-back footer-back__brand">
      <div class="brand"><span class="brand__mark"></span><span class="brand__name">TQB</span></div>
      <div class="brand__tag">Finance Department Service for Small Businesses</div>
    </div>
    <div class="abs footer-back footer-back__contact">Contact details: Address: 58 Dunmore Street, Carlisle, WA 6101<br>PO Box 2493, East Victoria Park, WA 6981<br>Tel: <b>(08) 6287 3914</b>;&nbsp; Mob: <b>0491 738 226</b></div>
  </section>

</div>
</body>
</html>
```